Instructional Tri-Fold Brochure for our Survival Membership Program

We need a tri-fold brochure that our new members will receive as a physical copy. The purpose of the brochure is to do 3 things:

1) Welcome them into the program
2) Educate them on the benefits
3) Educate them on the access instructions.

In addition to the brochure, they will receive a membership card. Attached is the brochure copy, the membership card design and the logo. Keep the color and style consistent with the membership card design.

You may use the images included in the attached document but you do not have to use all of them.

```html
<!DOCTYPE html>
<html lang="en">
<head>
<meta charset="utf-8">
<title>WildSteady Membership Tri-Fold</title>
<link rel="stylesheet" href="https://fonts.googleapis.com/css2?family=Lato:wght@400;700&family=Oswald:wght@500;600&display=swap">
<style>
  :root {
    --orange: #f39200;
    --lime: #c3dc22;
    --lime-deep: #8fb61a;
    --charcoal: #2b2b2b;
    --charcoal-soft: #3a3a3a;
    --paper: #f6f6f6;
    --paper-shade: #d9d9d9;
    --ink: #141414;
    --white: #ffffff;
    --page: #ececec;
  }
  * { margin: 0; padding: 0; box-sizing: border-box; }
  html, body { width: 1200px; height: 907px; overflow: hidden; background: var(--page); }
  .brochure {
    position: absolute; left: 55px; top: 66px; width: 1090px; height: 775px;
    overflow: hidden; box-shadow: 0 6px 18px rgba(0,0,0,.25);
    font-family: "Lato", sans-serif;
  }
  .brochure-art { position: absolute; inset: 0; }
  .about-title {
    position: absolute; left: 37px; width: 303px; top: 358px;
    text-align: right; font-family: "Oswald", sans-serif; font-weight: 600;
    font-size: 24px; letter-spacing: .5px; color: var(--ink);
  }
  .about-copy {
    position: absolute; left: 37px; top: 398px; width: 303px;
    font-size: 12px; line-height: 15.3px; color: var(--ink); text-align: justify;
  }
  .brand {
    position: absolute; display: flex; align-items: center; gap: 8px;
    font-family: "Lato", sans-serif; font-weight: 700; font-size: 25px; color: var(--orange);
  }
  .brand-dot { width: 32px; height: 32px; border-radius: 50%; background: var(--orange); }
  .brand--contact { left: 418px; top: 280px; }
  .brand--card { left: 778px; top: 150px; }
  .contact-phone {
    position: absolute; left: 448px; top: 332px; display: flex; align-items: center; gap: 8px;
    font-family: "Oswald", sans-serif; font-weight: 600; font-size: 30px; color: var(--white);
  }
  .contact-line {
    position: absolute; left: 435px; display: flex; align-items: center; gap: 5px;
    font-size: 15px; color: var(--white);
  }
  .contact-line--mail { top: 387px; left: 445px; }
  .contact-line--web { top: 422px; }
  .member-name {
    position: absolute; left: 745px; width: 330px; top: 196px; text-align: center;
    font-family: "Oswald", sans-serif; font-weight: 600; font-size: 46px;
    letter-spacing: 1px; color: var(--orange);
  }
  .member-id {
    position: absolute; left: 745px; width: 330px; top: 258px; text-align: center;
    font-size: 42px; color: var(--ink); letter-spacing: .5px;
  }
  .member-site {
    position: absolute; left: 745px; width: 330px; top: 309px; text-align: center;
    font-size: 13px; letter-spacing: 3.2px; color: var(--ink);
  }
</style>
</head>
<body>
<main class="brochure">
  <svg class="brochure-art" width="1090" height="775" viewBox="0 0 1090 775" aria-hidden="false">
    <defs>
      <linearGradient id="lime-panel" x1="0" y1="0" x2="0" y2="1">
        <stop offset="0" stop-color="#d3e62a"/>
        <stop offset="1" stop-color="#9cc01b"/>
      </linearGradient>
      <linearGradient id="charcoal-panel" x1="0" y1="0" x2="0" y2="1">
        <stop offset="0" stop-color="#262626"/>
        <stop offset="1" stop-color="#3e3e3e"/>
      </linearGradient>
      <linearGradient id="paper-panel" x1="0" y1="0" x2="1" y2="0">
        <stop offset="0" stop-color="#d6d6d6"/>
        <stop offset=".35" stop-color="#f6f6f6"/>
        <stop offset="1" stop-color="#ffffff"/>
      </linearGradient>
      <linearGradient id="jungle-tones" x1="0" y1="0" x2="1" y2="1">
        <stop offset="0" stop-color="#3e6b2a"/>
        <stop offset=".5" stop-color="#5c8a4a"/>
        <stop offset="1" stop-color="#6f8fa0"/>
      </linearGradient>
      <linearGradient id="summit-tones" gradientUnits="userSpaceOnUse" x1="1000" y1="380" x2="800" y2="775">
        <stop offset="0" stop-color="#7fb9e6"/>
        <stop offset=".3" stop-color="#c6b89c"/>
        <stop offset=".45" stop-color="#3b3228"/>
        <stop offset="1" stop-color="#121212"/>
      </linearGradient>
      <polygon id="jungle-edge" points="0,0 620,0 606,10 592,18 578,30 560,40 545,52 528,62 510,74 494,84 478,96 460,104 445,118 428,126 410,140 395,148 380,160 362,170 348,184 330,192 315,206 300,214 280,228 268,238 250,246 236,262 220,270 205,282 190,292 172,300 160,318 150,322 130,332 118,344 100,352 90,360 72,370 60,378 45,385 30,404 18,400 0,408"/>
      <polygon id="sky-edge" points="620,0 640,14 655,18 668,30 685,36 700,48 716,52 730,62 750,60 770,66 790,62 810,68 830,66 850,76 870,74 890,84 910,80 930,90 950,92 970,100 990,98 1010,108 1030,110 1050,116 1070,114 1090,125 1090,0"/>
      <polygon id="summit-edge" points="370,715 385,708 400,700 420,696 435,684 455,680 470,668 490,662 510,650 530,646 550,634 568,630 585,620 605,612 620,600 640,596 660,584 678,578 695,566 715,560 735,548 752,540 770,532 790,526 808,516 825,506 845,498 862,490 880,480 900,474 918,462 935,456 955,446 972,438 990,428 1010,420 1028,408 1045,398 1062,388 1078,378 1090,365 1090,775 370,775"/>
    </defs>

    <rect class="panel panel--about" x="0" y="0" width="370" height="775" fill="url(#lime-panel)"/>
    <rect class="panel panel--contact" x="370" y="0" width="365" height="775" fill="url(#charcoal-panel)"/>
    <rect class="panel panel--card" x="735" y="0" width="355" height="775" fill="url(#paper-panel)"/>

    <g class="torn-band torn-band--top">
      <use href="#sky-edge" transform="translate(0,17)" fill="var(--lime)"/>
      <use href="#sky-edge" transform="translate(0,9)" fill="var(--orange)"/>
      <use href="#sky-edge" transform="translate(0,4)" fill="#111"/>
      <use href="#sky-edge" fill="var(--white)"/>
    </g>

    <g class="torn-band torn-band--jungle">
      <use href="#jungle-edge" transform="translate(10,16)" fill="var(--lime-deep)"/>
      <use href="#jungle-edge" transform="translate(5,9)" fill="var(--orange)"/>
    </g>
    <g class="photo photo--family" role="img" aria-label="Photo: mother hiking through a green jungle with her child in a back carrier">
      <use href="#jungle-edge" fill="url(#jungle-tones)"/>
    </g>

    <g class="torn-band torn-band--summit">
      <use href="#summit-edge" transform="translate(0,-16)" fill="var(--lime)"/>
      <use href="#summit-edge" transform="translate(0,-8)" fill="var(--orange)"/>
    </g>
    <g class="photo photo--summit" role="img" aria-label="Photo: hiker silhouette raising an arm on a mountain summit above a hazy valley">
      <use href="#summit-edge" fill="url(#summit-tones)"/>
    </g>
  </svg>

  <h2 class="about-title">ABOUT US</h2>
  <p class="about-copy">Lorem ipsum dolor sit amet, nec dicit nostrud id. Id tantas voluptatibus mei, eos in illum legimus. Esse mutat nobis mei in, sed ut possit civibus, vim in dicat ocurreret. Ius et tota everti, ut persius impedit omittam vis. Sint harum blandit ut vix.<br>Per an erat animal detraxit, omnes dolore no eum. No nulla scripta iracundia vim, vel ut alii saepe efficiantur, mea accusamus interpretaris an. Saperet sensibus definitionem has ut, ut quando fabulas invidunt eam. Graece equidem definitiones ut eam, usu verear fabulas constituam no. His harum sadipscing ei.<br>Ad mel prima omittam complectitur, cum summo tacimates et. Vis homero inciderint in, an vix sint detraxit democritum. Et dissentias sadipscing vix. Vis ubique patrioque constituam te, cu possim eligendi accusamus duo. Eos labore definiebas an, dicant argumentum ut ius, congue iuvaret dissentiunt eum at.<br>Sit cu deleniti vivendum. At erat aperiri dolores vim. Hinc legere splendide cum cu, at unum suscipit pri, pro no vocibus eligendi. Pri ei soleat oblique disputationi. Ne etiam verear definiebas vel, ad mel putant menandri, erroribus temporibus te vis.</p>

  <div class="brand brand--contact"><span class="brand-dot"></span>WildSteady</div>
  <div class="contact-phone">
    <svg width="20" height="20" viewBox="0 0 20 20" aria-hidden="true">
      <rect width="20" height="20" rx="3" fill="var(--orange)"/>
      <path d="M6 4.5 L8.3 4.5 L9 7.6 L7.6 8.6 C8.4 10.3 9.7 11.6 11.4 12.4 L12.4 11 L15.5 11.7 L15.5 14 C15.5 14.8 14.8 15.5 14 15.5 C8.8 15.2 4.8 11.2 4.5 6 C4.5 5.2 5.2 4.5 6 4.5 Z" fill="#222"/>
    </svg>
    0198765432
  </div>
  <div class="contact-line contact-line--mail">
    <svg width="12" height="9" viewBox="0 0 12 9" aria-hidden="true"><rect x=".5" y=".5" width="11" height="8" fill="none" stroke="var(--orange)"/><path d="M.5 .5 L6 5 L11.5 .5" fill="none" stroke="var(--orange)"/></svg>
    www.wildsteady@mail.com
  </div>
  <div class="contact-line contact-line--web">
    <svg width="13" height="13" viewBox="0 0 13 13" aria-hidden="true"><circle cx="6.5" cy="6.5" r="5.8" fill="none" stroke="var(--orange)" stroke-width="1.2"/><ellipse cx="6.5" cy="6.5" rx="2.5" ry="5.8" fill="none" stroke="var(--orange)"/><path d="M.7 6.5 H12.3" stroke="var(--orange)"/></svg>
    www.wildsteadyclub.com
  </div>

  <div class="brand brand--card"><span class="brand-dot"></span>WildSteady</div>
  <h1 class="member-name">MARCUS HOLDEN</h1>
  <p class="member-id">VIP-XXXXXXX</p>
  <p class="member-site">www.wildsteadyclub.com</p>
</main>
</body>
</html>
```